Online Prescription Eyeglass Lens Company Needs a Website

*Update new name to ClearPair. Thx

We are eye doctors with a lab that need a website for a new company based in Southern California called ClearPair. We replace old prescription lenses with new ones next day for most lenses. Patients select the lenses and give us the prescription. We then send a box with a prepaid shipping label. Place the frames in the box and drop them in the mail to our lab. We will custom make new lenses, fit them back into your frames and send them back to you. We would like to compete with www.vizora.com and offer affordable lenses for single vision, bifocal, progressive, sunglass lenses at an affordable price with next day shipping.
Updates

Hi Designers, We have a new name called ClearPair. Can we have the website design reflect the new name and we'll pick our favorites. Thx

Update: The new name is OptiNova . I have not made very many changes or feedback to the submissions because we were bidding for a .com. We won and our new name is OptiNova . This is the last name change.. Please have the website reflect the new name and I'll be providing feedback on the websites . ( I have a separate project for the logo people are working on, so don't worry about creating a logo). Look forward to the submissions. Thanks everyone.

Hi, Just leave the name as ClearPair for now. I will narrow down top designs tonight. Thx

Target Market(s)

Anyone that wears prescription or nonprescription glasses or sunglasses that want next day shipping.

Industry/Entity Type

Eyewear

Number of Pages Required

4 page

Font styles to use
Serif

Colors

Designer to choose colors to be used in the design.

Requirements
Must have
• I need a website that can compete with https://www.vizora.com/.
• We are different from vizora because we can offer same day service or next day shipping.
• It needs to have website that offers the lenses available listed below.
• Needs to be able to upload a prescription and payment feature.
• Pictures of different types of options with small info about each lens option.
• Template Pricing (just use numbers from $79-$179 for now)
• SINGLE VISION LENSES
• HIGH INDEX LENSES
• READING LENSES
• DIGITAL HD PROGRESSIVE LENSES
• RX & NON-RX SUNGLASSES
• RX & NON-RX POLARIZED SUNGLASSES
• COMPUTER LENSES
• TRANSITION LENSES
• BI-FOCAL LENSES

```html
<!DOCTYPE html>
<html lang="en">
<head>
<meta charset="utf-8">
<title>ClearPair – Prescription Lenses, Next Day</title>
<link rel="stylesheet" href="https://fonts.googleapis.com/css2?family=Cabin:ital,wght@0,400;0,500;0,600;0,700;1,600&family=Oswald:wght@500;700&family=Roboto+Condensed:wght@300;700&display=swap">
<style>
:root{
  --navy:#1b2840;
  --blue:#1a5fc7;
  --blue-bright:#0f5cc6;
  --ink:#1d1d1d;
  --muted:#6e6e6e;
  --white:#ffffff;
  --footer-text:#8a93a6;
}
*{box-sizing:border-box;margin:0;padding:0}
html,body{width:1200px;height:2332px;overflow:hidden;background:var(--white)}
body{position:relative;font-family:"Cabin",sans-serif;color:var(--ink)}
.abs{position:absolute}

/* nav */
.site-nav{left:0;top:0;width:1200px;height:65px;background:var(--navy)}
.brand{font-family:"Oswald",sans-serif;font-weight:700;color:var(--white);font-size:29px;letter-spacing:.3px}
.site-nav .brand{left:158px;top:11px}
.menu{left:604px;top:0;height:65px}
.menu a{color:var(--white);text-decoration:none;font-size:11px;font-weight:500;letter-spacing:.2px;text-transform:uppercase;position:absolute;white-space:nowrap}
.menu .home{left:0;top:22px}
.menu .m1{left:47px;top:26px}
.menu .m2{left:128px;top:26px}
.menu .m3{left:218px;top:26px}
.menu .m4{left:297px;top:26px}
.menu .user{left:398px;top:22px}

/* hero */
.hero{left:0;top:65px;width:1200px;height:495px;
  background:
    radial-gradient(ellipse 60% 45% at 50% 42%,rgba(120,130,90,.55) 0%,rgba(80,88,60,0) 70%),
    radial-gradient(ellipse 30% 55% at 18% 35%,rgba(95,110,70,.55),rgba(0,0,0,0) 70%),
    radial-gradient(ellipse 30% 55% at 82% 35%,rgba(95,110,70,.5),rgba(0,0,0,0) 70%),
    linear-gradient(180deg,#2f3328 0%,#45493a 30%,#4c4c3b 55%,#3b3024 72%,#6b4630 84%,#8a5a3a 92%,#4a2f20 100%)}
.hero-shade{left:0;top:0;width:1200px;height:495px;background:radial-gradient(ellipse 75% 80% at 50% 45%,rgba(0,0,0,0) 40%,rgba(10,10,8,.45) 100%)}
.hero-title{left:0;top:156px;width:1200px;text-align:center;color:var(--white);font-style:italic;font-weight:600;font-size:40px;letter-spacing:.3px;text-shadow:0 2px 6px rgba(0,0,0,.35)}
.hero-rule{left:553px;top:228px;width:94px;height:3px;background:var(--blue-bright)}
.btn{display:flex;align-items:center;justify-content:center;border-radius:22px;font-size:13px;font-weight:600;color:var(--white);text-decoration:none}
.btn-ghost{left:382px;top:278px;width:210px;height:42px;border:2px solid var(--white)}
.btn-solid{left:608px;top:278px;width:208px;height:42px;background:var(--blue-bright);text-transform:uppercase;font-size:12px}

/* steps band */
.steps{left:0;top:560px;width:1200px;height:115px;
  background:
    linear-gradient(120deg,rgba(255,255,255,.06) 0 22%,rgba(0,0,0,0) 22% 48%,rgba(255,255,255,.05) 48% 70%,rgba(0,0,0,.04) 70% 100%),
    linear-gradient(135deg,#2c6fd0 0%,#1f5ec2 50%,#2a6acb 100%)}
.step{top:0;height:115px;display:flex;align-items:center;gap:12px;color:var(--white);font-size:17px}
.step-arrow{top:46px}

/* products row */
.product-photo{left:0;top:675px;width:600px;height:432px;
  background:
    radial-gradient(ellipse 45% 35% at 50% 48%,rgba(40,40,40,.35),rgba(0,0,0,0) 70%),
    radial-gradient(ellipse 70% 60% at 60% 40%,#9a9996 0%,rgba(154,153,150,0) 70%),
    repeating-linear-gradient(172deg,rgba(255,255,255,.03) 0 3px,rgba(0,0,0,.03) 3px 7px),
    linear-gradient(135deg,#5e5d5b 0%,#858481 50%,#5a5957 100%)}
.products{left:600px;top:675px;width:600px;height:432px;background:var(--white)}
.products-title{left:0;top:30px;width:456px;text-align:center;font-size:23px;font-weight:500;letter-spacing:.2px}
.pager{top:31px;width:22px;height:22px;border:1px solid #d4d4d4;display:flex;align-items:center;justify-content:center}
.products-sub{left:0;top:80px;width:456px;text-align:center;font-size:12px;line-height:19px;text-transform:uppercase}
.card{top:127px;width:200px;height:194px;border:1px solid #dcdcdc;padding:6px;background:var(--white);box-shadow:0 1px 3px rgba(0,0,0,.08)}
.card .pic{width:100%;height:100%}
.card-name{top:345px;width:230px;text-align:center;font-size:13px;font-weight:600;text-transform:uppercase}
.card-desc{top:365px;width:230px;text-align:center;font-size:11px;line-height:18px;color:var(--muted)}

/* shipping row */
.shipping{left:0;top:1107px;width:600px;height:351px;background:var(--white)}
.frames-photo{left:0;top:8px;width:260px;height:220px;
  background:
    radial-gradient(ellipse 55% 40% at 35% 45%,rgba(110,70,35,.85) 0%,rgba(150,110,70,.45) 45%,rgba(255,255,255,0) 75%),
    radial-gradient(ellipse 35% 30% at 72% 30%,rgba(90,60,30,.6),rgba(255,255,255,0) 75%)}
.ship-kicker{left:120px;top:110px;width:494px;text-align:center;font-family:"Roboto Condensed",sans-serif;font-weight:300;font-size:27px;color:#333;text-transform:uppercase}
.ship-title{left:120px;top:170px;width:494px;text-align:center;font-family:"Roboto Condensed",sans-serif;font-weight:700;font-size:46px;line-height:58px;color:#111;text-transform:uppercase}
.features{left:0;top:1458px;width:600px;height:81px;background:var(--navy)}
.feature{top:14px;width:160px;text-align:center;color:var(--white);font-size:9px;text-transform:uppercase;letter-spacing:.2px}
.feature svg{display:block;margin:0 auto 8px}
.family-photo{left:600px;top:1107px;width:600px;height:432px;
  background:
    radial-gradient(ellipse 28% 32% at 28% 52%,#e6b89c 0%,rgba(230,184,156,0) 75%),
    radial-gradient(ellipse 24% 28% at 66% 38%,#f0cdb6 0%,rgba(240,205,182,0) 75%),
    radial-gradient(ellipse 30% 25% at 62% 90%,#d9a6a0 0%,rgba(217,166,160,0) 75%),
    radial-gradient(ellipse 40% 50% at 10% 20%,#6a3a24 0%,rgba(106,58,36,0) 75%),
    radial-gradient(ellipse 40% 45% at 85% 15%,#8a4a2c 0%,rgba(138,74,44,0) 75%),
    linear-gradient(135deg,#5a3325 0%,#9b6a52 45%,#b98670 70%,#6a4034 100%)}

/* intro */
.intro-title{left:0;top:1597px;width:1200px;text-align:center;font-size:25px;font-weight:500}
.intro-rule{left:569px;top:1639px;width:62px;height:3px;background:#8fb0de}
.intro-box{left:160px;top:1675px;width:878px;height:361px;background:var(--white);border:12px solid #f3f4f6}
.intro-copy{left:64px;top:53px;width:420px;text-align:center;font-size:10.5px;line-height:13px;color:#444}
.intro-copy p{margin-bottom:13px}
.btn-start{left:154px;top:252px;width:209px;height:42px;background:var(--blue-bright);text-transform:uppercase;font-size:12px}
.doctor-photo{left:512px;top:30px;width:320px;height:277px;
  background:
    radial-gradient(ellipse 22% 18% at 22% 50%,rgba(210,50,40,.55),rgba(210,50,40,0) 75%),
    radial-gradient(ellipse 30% 40% at 80% 30%,#d9b8a2 0%,rgba(217,184,162,0) 75%),
    radial-gradient(ellipse 25% 30% at 88% 85%,#6d8fc4 0%,rgba(109,143,196,0) 75%),
    radial-gradient(ellipse 35% 45% at 8% 35%,#5f656d 0%,rgba(95,101,109,0) 75%),
    linear-gradient(135deg,#eef0f2 0%,#dfe3e7 50%,#cfd5dc 100%)}

/* footer */
.site-footer{left:0;top:2098px;width:1200px;height:187px;background:var(--navy)}
.site-footer .brand{left:160px;top:38px;font-size:28px}
.footer-copy{left:162px;top:106px;width:490px;font-size:10px;line-height:12.5px;color:var(--footer-text)}
.footer-copy p{margin-bottom:10px}
.footer-head{top:26px;color:var(--white);font-size:12px;font-weight:600;text-transform:uppercase}
.footer-links{left:724px;top:56px;list-style:none;font-size:11px;line-height:19.4px}
.footer-links a{color:var(--footer-text);text-decoration:none}
.footer-email{left:859px;top:50px;display:flex;align-items:center;gap:10px;font-size:10px;color:var(--footer-text);text-transform:uppercase}
.bottom-bar{left:0;top:2285px;width:1200px;height:47px;background:var(--blue-bright)}
.copyright{left:160px;top:17px;font-size:10px;color:#cfe0ff}
.copyright b{color:var(--white);font-weight:600}
.find-us{left:817px;top:15px;font-size:12px;color:#a9c6f5;text-transform:uppercase;letter-spacing:.3px}
.social{left:903px;top:11px;display:flex;gap:5px}
.social span{width:25px;height:25px;border-radius:50%;border:1.5px solid var(--white);display:block}
</style>
</head>
<body>

<header class="abs site-nav">
  <div class="abs brand">ClearPair</div>
  <nav class="abs menu">
    <a class="home" href="#" aria-label="Home"><svg width="20" height="18" viewBox="0 0 20 18"><path d="M10 1 1 9h3v8h4.5v-5h3v5H16V9h3z" fill="#fff"/></svg></a>
    <a class="m1" href="#">Products</a>
    <a class="m2" href="#">My Account</a>
    <a class="m3" href="#">Checkout</a>
    <a class="m4" href="#">Contact Us</a>
    <a class="user" href="#" aria-label="Account"><svg width="16" height="18" viewBox="0 0 16 18"><circle cx="8" cy="5" r="4.2" fill="#fff"/><path d="M0 18c0-5 3.5-7.5 8-7.5s8 2.5 8 7.5z" fill="#fff"/></svg></a>
  </nav>
</header>

<section class="abs hero" role="img" aria-label="Photo of dark eyeglasses resting on a wooden rail with a blurred forest behind">
  <div class="abs hero-shade"></div>
  <h1 class="abs hero-title">Welcome To The Harborline Opticals</h1>
  <div class="abs hero-rule"></div>
  <a class="abs btn btn-ghost" href="#">Choose Your Lense</a>
  <a class="abs btn btn-solid" href="#">See How Its Done</a>
</section>

<section class="abs steps">
  <div class="abs step" style="left:160px">
    <svg width="46" height="30" viewBox="0 0 46 30" fill="none" stroke="#fff" stroke-width="2.4"><path d="M3 10 8 3M43 10l-5-7"/><rect x="3" y="10" width="17" height="14" rx="7"/><rect x="26" y="10" width="17" height="14" rx="7"/><path d="M20 15c2-2 4-2 6 0"/></svg>
    <span>Select Lenses</span>
  </div>
  <svg class="abs step-arrow" style="left:367px" width="84" height="24" viewBox="0 0 84 24" fill="none" stroke="#fff" stroke-width="2.4"><path d="M2 12h70" stroke-dasharray="8 6"/><path d="M70 3l10 9-10 9"/></svg>
  <div class="abs step" style="left:493px">
    <svg width="66" height="40" viewBox="0 0 66 40" fill="none" stroke="#fff" stroke-width="2.2"><path d="M3 3h30v20H16l-7 6v-6H3z"/><path d="M14 9q4-4 7 0t-4 6v2M17 20v1"/><path d="M37 12h26v18h-6v6l-7-6H37z"/><circle cx="45" cy="21" r="1.3" fill="#fff"/><circle cx="50" cy="21" r="1.3" fill="#fff"/><circle cx="55" cy="21" r="1.3" fill="#fff"/></svg>
    <span>Send Prescription</span>
  </div>
  <svg class="abs step-arrow" style="left:754px" width="84" height="24" viewBox="0 0 84 24" fill="none" stroke="#fff" stroke-width="2.4"><path d="M2 12h70" stroke-dasharray="8 6"/><path d="M70 3l10 9-10 9"/></svg>
  <div class="abs step" style="left:881px">
    <svg width="62" height="26" viewBox="0 0 62 26" fill="none" stroke="#fff" stroke-width="2.4"><circle cx="16" cy="13" r="10"/><circle cx="46" cy="13" r="10"/><path d="M26 12q5-4 10 0M6 12H1M56 12h5"/></svg>
    <span>New Lense</span>
  </div>
</section>

<div class="abs product-photo" role="img" aria-label="Photo of round black eyeglasses on a grey wooden table"></div>

<section class="abs products">
  <h2 class="abs products-title">OUR PRODUCTS</h2>
  <span class="abs pager" style="left:391px"><svg width="6" height="8" viewBox="0 0 6 8"><path d="M5 1 1 4l4 3" fill="none" stroke="#888"/></svg></span>
  <span class="abs pager" style="left:416px"><svg width="6" height="8" viewBox="0 0 6 8"><path d="M1 1l4 3-4 3" fill="none" stroke="#888"/></svg></span>
  <p class="abs products-sub">Single Vision<br>Lenses</p>
  <div class="abs card" style="left:20px"><div class="pic" role="img" aria-label="Portrait photo of a woman wearing black-framed glasses" style="background:radial-gradient(ellipse 45% 50% at 50% 58%,#b07a5a 0%,rgba(176,122,90,0) 80%),radial-gradient(ellipse 60% 30% at 50% 5%,#3a2418 0%,rgba(58,36,24,0) 80%),linear-gradient(135deg,#e4e4e4,#cfc7c2)"></div></div>
  <div class="abs card" style="left:239px"><div class="pic" role="img" aria-label="Portrait photo of a woman with red lips wearing tortoiseshell glasses" style="background:radial-gradient(ellipse 40% 48% at 52% 55%,#e0b9a2 0%,rgba(224,185,162,0) 80%),radial-gradient(ellipse 12% 8% at 55% 78%,#c8242a 0%,rgba(200,36,42,0) 90%),radial-gradient(ellipse 60% 35% at 50% 8%,#5a3222 0%,rgba(90,50,34,0) 80%),linear-gradient(135deg,#f0f0f0,#d8d8da)"></div></div>
  <h3 class="abs card-name" style="left:5px">Single Vision Lenses</h3>
  <p class="abs card-desc" style="left:5px">Single vision lenses are prescribed<br>if you need correction...</p>
  <h3 class="abs card-name" style="left:224px">High Index Lenses</h3>
  <p class="abs card-desc" style="left:224px">Single vision lenses are prescribed<br>if you need correction...</p>
</section>

<section class="abs shipping">
  <div class="abs frames-photo" role="img" aria-label="Photo of tortoiseshell eyeglass frames"></div>
  <p class="abs ship-kicker">Next Day Shipping</p>
  <h2 class="abs ship-title">Nonprescription<br>Glasses</h2>
</section>

<section class="abs features">
  <div class="abs feature" style="left:106px">
    <svg width="28" height="28" viewBox="0 0 28 28" fill="none" stroke="#fff" stroke-width="2"><rect x="3" y="5" width="22" height="20" rx="2"/><path d="M3 11h22M9 2v6M19 2v6"/><path d="M11 15h6l-4 8" stroke-width="2.4"/></svg>
    Open 7 Day
  </div>
  <div class="abs feature" style="left:262px">
    <svg width="40" height="28" viewBox="0 0 40 28" fill="none" stroke="#fff" stroke-width="2"><circle cx="10" cy="15" r="8"/><circle cx="30" cy="15" r="8"/><path d="M18 14q2-3 4 0M2 14H0M38 14h2"/></svg>
    Licensed Optometrist
  </div>
  <div class="abs feature" style="left:437px">
    <svg width="24" height="28" viewBox="0 0 24 28"><circle cx="12" cy="8" r="6" fill="#fff"/><path d="M1 27c0-8 5-12 11-12s11 4 11 12z" fill="#fff"/></svg>
    Contact Fitted
  </div>
</section>

<div class="abs family-photo" role="img" aria-label="Photo of a smiling mother and daughter both wearing glasses"></div>

<section>
  <h2 class="abs intro-title">Start Seeing Clearly</h2>
  <div class="abs intro-rule"></div>
  <div class="abs intro-box">
    <div class="abs intro-copy">
      <p>Lorem ipsum dolor sit amet, consectetur adipiscing elit, sed do eiusmod tempor incididunt ut labore et dolore magna aliqua. Ut enim ad minim veniam, quis nostrud exercitation ullamco laboris nisi ut aliquip ex ea commodo consequat.</p>
      <p>Duis aute irure dolor in reprehenderit in voluptate velit esse cillum dolore eu fugiat nullaLorem ipsum dolor sit amet, consectetur adipiscing elit, sed do eiusmod tempor incididunt ut labore et dolore magna aliqua. Ut enim ad minim veniam, quis nostrud exercitation ullamco laboris nisi ut aliquip ex ea commodo consequat.</p>
      <p>Duis aute irure dolor in reprehenderit in voluptate velit esse cillum dolore eu fugiat nulla</p>
    </div>
    <a class="abs btn btn-start" href="#">Lets Get Started</a>
    <div class="abs doctor-photo" role="img" aria-label="Photo of an optometrist adjusting a trial lens frame"></div>
  </div>
</section>

<footer class="abs site-footer">
  <div class="abs brand">ClearPair</div>
  <div class="abs footer-copy">
    <p>Lorem ipsum dolor sit amet, consectetur adipiscing elit, sed do eiusmod tempor incididunt ut labore et dolore magna aliqua. Ut enim ad minim veniam, quis nostrud exercitation ullamco laboris nisi ut aliquip ex ea commodo consequat.</p>
    <p>Duis aute irure dolor in reprehenderit in voluptate velit esse cillum dolore eu fugiat nulla</p>
  </div>
  <h4 class="abs footer-head" style="left:724px">About</h4>
  <ul class="abs footer-links">
    <li><a href="#">Home</a></li>
    <li><a href="#">Products</a></li>
    <li><a href="#">My Account</a></li>
    <li><a href="#">Checkout</a></li>
    <li><a href="#">Contact Us</a></li>
  </ul>
  <h4 class="abs footer-head" style="left:859px">Contact Us</h4>
  <div class="abs footer-email">
    <svg width="14" height="10" viewBox="0 0 14 10"><rect width="14" height="10" fill="#8a93a6"/><path d="M0 0l7 5 7-5" fill="none" stroke="#1b2840"/></svg>
    Email Us
  </div>
</footer>

<div class="abs bottom-bar">
  <p class="abs copyright">Copyrights© 2017 <b>ClearPair</b> Allrights are Reserved</p>
  <p class="abs find-us">Find Us On</p>
  <div class="abs social" aria-label="Social links"><span></span><span></span><span></span><span></span><span></span></div>
</div>

</body>
</html>
```